Mortgage Protection Insurance Flyer

The target audience are new home owners so the design needs to be clean and simple.

This a primarily for Final Expense Insurance, but need an area where it says "We Also Specialize In:"
- Medicare Supplement Insurance (MediGap)
- Annuities
- Final Expense

All flyer versions need to be editable. Colors to be used are red, white or black. Refer to my website for colors and photos (harborvaleassurance.com). Will attach my logo and a flyer that I found online that is the format that I am looking for (for 8.5 in. x 11 in version). Need flyer in standard letter size 8.5 in. x11 in. but also in 8.5 in. x 5.5 in and 5.0 in. x 8.0 in. All sizes to be portrait oriented. If picked as winning design, need all flyer versions in full color, also in grey scale and files in all industry file types.

Content can be taken from my website..... harborvaleassurance.com

Do NOT submit if you are not willing to provide all versions as described above for the original project price.

Must use royalty-free stock photos please.

Target Market(s)

New homeowners looking for insurance to protect there mortgage payments

Industry/Entity Type

Life Insurance

Colors
f69fa3

Requirements
Must have
• Colors to be used are red, white or black.
• Need flyer in standard letter size 8.5 in. x11 in. but also in 3.5 in. x 8.5 in (Full Bleed 3.75 in by 8.75 in.) and 4.0 in. x 6.0 in. (Full Bleed 4.12 in x 6.12 in) Each design tailored to the size dimensions (So no squeezing 8.5 x 11 design into a 4.0 x 6.0 space.) All sizes to be portrait oriented. If picked as winning design, need all flyer versions in full color, also in grey scale and files in all file types.
• Do not need physical address on flyer, do need email address on flyer though - tkerlow@harborvaleassurance.com
• So phone number should be prominent, email address and website address should also be contact area.
• If you can not agree to terms above, do not submit any designs.
• Need facebook & twitter logos somewhere in contact info area.
Nice to have
• See sample flyers I have attached.
• White background with red used as primary graphic color and black used as secondary graphic if needed.
• font to be used should similar to one used in logo.

```html
<!DOCTYPE html>
<html lang="en">
<head>
<meta charset="utf-8">
<title>Harborvale Assurance – Final Expense Flyer</title>
<link href="https://fonts.googleapis.com/css2?family=Anton&family=Roboto:wght@400;700;900&family=Cabin:wght@400;600&display=swap" rel="stylesheet">
<style>
:root{
  --red:#e30613;
  --red-dark:#9e1a1e;
  --black:#231f20;
  --ink:#3a3a3a;
  --grey-bar:#cfcfcf;
  --board-grey:#dedede;
  --board-pink:#ffcfcf;
  --white:#ffffff;
}
*{margin:0;padding:0;box-sizing:border-box}
html,body{width:780px;height:1200px;overflow:hidden}
body{position:relative;background:var(--board-pink);font-family:"Cabin",sans-serif;color:var(--ink)}
.board-top{position:absolute;left:0;top:0;width:780px;height:722px;background:var(--board-grey)}
.sheet{position:absolute;background:var(--white);overflow:hidden}
.layer{position:absolute;left:0;top:0}
.photo{position:absolute;background:linear-gradient(90deg,#ffffff 0%,#eef1ef 22%,#b7cdb0 42%,#e9cdb5 60%,#8da96f 80%,#c3d9ee 100%)}
.brand{position:absolute;font-family:"Roboto",sans-serif;font-weight:900;color:var(--black);white-space:nowrap}
.headline{position:absolute;font-family:"Anton",sans-serif;font-weight:400;line-height:1.02;color:var(--black)}
.headline .accent{color:var(--red)}
.headline .sub{display:block;line-height:1.15}
.benefits{position:absolute;background:linear-gradient(180deg,var(--red) 0%,#c8141b 70%,var(--red-dark) 100%);border-radius:8px;color:var(--white);font-family:"Roboto",sans-serif}
.tab{position:absolute;background:#333;color:var(--white);font-family:"Roboto",sans-serif;font-weight:700;border-radius:0 6px 6px 0;padding-left:4px;white-space:nowrap}
.ticks{list-style:none}
.ticks li{position:relative}
.ticks li::before{content:"";position:absolute;left:0;border:.8px solid currentColor;border-radius:50%}
.ticks li::after{content:"";position:absolute;border-right:.8px solid currentColor;border-bottom:.8px solid currentColor;transform:rotate(45deg)}
.red-ticks li::before,.red-ticks li::after{border-color:var(--red)}
.title-red{position:absolute;font-family:"Roboto",sans-serif;font-weight:700;color:var(--red);white-space:nowrap}
.copy{position:absolute}
.rate{position:absolute;display:flex;font-family:"Roboto",sans-serif;font-weight:700}
.rate .label{background:var(--grey-bar);color:var(--black)}
.rate .value{background:var(--red);color:var(--white);text-align:center}
.note{position:absolute;color:#555}
.contact{position:absolute;color:var(--white);font-family:"Roboto",sans-serif;font-weight:700;white-space:nowrap}
.icon-ring{position:absolute;border:1px solid var(--white);border-radius:50%}
.social{position:absolute;display:flex;gap:1.5px}
.social span{display:block;background:var(--white)}
.flyer .ticks li::before{top:0.5px;width:6px;height:6px}
.flyer .ticks li::after{left:2.1px;top:1.4px;width:1.6px;height:3px}
.flyer .red-ticks li::before{top:2.2px}
.flyer .red-ticks li::after{top:3.1px}
.card-front .ticks li::before{top:0.3px;width:4.4px;height:4.4px}
.card-front .ticks li::after{left:1.6px;top:1px;width:1.1px;height:2.2px}
.card-back .ticks li::before{top:0.8px;width:4.2px;height:4.2px}
.card-back .ticks li::after{left:1.5px;top:1.5px;width:1.1px;height:2.1px}
</style>
</head>
<body>
<div class="board-top"></div>

<section class="sheet flyer" style="left:202px;top:140px;width:376px;height:484px;">
  <div class="photo" role="img" aria-label="Photo of a smiling young couple outdoors, man giving woman a piggyback ride" style="left:0;top:0;width:376px;height:200px;"></div>
  <svg class="layer" width="376" height="484" viewBox="0 0 376 484" aria-hidden="true">
    <defs><linearGradient id="footRed" x1="0" y1="0" x2="0" y2="1"><stop offset="0" stop-color="#e30613"/><stop offset="1" stop-color="#9e1a1e"/></linearGradient></defs>
    <path d="M0 0 H204 C180 42 114 78 0 80 Z" fill="#fff"/>
    <path d="M0 76 C110 74 175 40 198 0" fill="none" stroke="#231f20" stroke-width="4"/>
    <path d="M0 82 C114 80 182 46 208 0" fill="none" stroke="#e30613" stroke-width="2"/>
    <path d="M0 188 C100 212 250 184 376 174 V484 H0 Z" fill="#fff"/>
    <path d="M0 180 C100 204 250 176 376 166" fill="none" stroke="#231f20" stroke-width="5"/>
    <path d="M0 187 C100 211 250 183 376 173" fill="none" stroke="#e30613" stroke-width="2.5"/>
    <path d="M0 440 C120 408 270 438 376 423 V484 H0 Z" fill="url(#footRed)"/>
    <path d="M0 433 C120 401 270 431 376 416" fill="none" stroke="#231f20" stroke-width="3"/>
  </svg>
  <div class="brand" style="left:20px;top:26px;font-size:10.5px;">Harborvale Assurance</div>
  <h1 class="headline" style="left:19px;top:98px;font-size:28px;">OUR<br><span class="accent">PLANS ARE</span><span class="sub" style="font-size:17px;">BASED ON YOURS</span></h1>

  <div class="benefits" style="left:218px;top:161px;width:143px;height:172px;">
    <ul class="ticks" style="position:absolute;left:11px;top:38px;width:126px;font-size:5.6px;line-height:7.2px;font-weight:500;">
      <li style="padding-left:11px;margin-bottom:7px;">All plans we offer are state regulated</li>
      <li style="padding-left:11px;margin-bottom:7px;">Relatively low monthly premiums</li>
      <li style="padding-left:11px;margin-bottom:7px;">Premiums can never increase</li>
      <li style="padding-left:11px;margin-bottom:7px;">Your policy can never be cancelled as long as you pay your premium</li>
      <li style="padding-left:11px;margin-bottom:7px;">No medical exams</li>
      <li style="padding-left:11px;margin-bottom:7px;">Guaranteed Death Benefit</li>
      <li style="padding-left:11px;">Many policies we offer are Guaranteed Acceptance, "Day 1" coverage, have a child/grandchild rider and/or have an accelerated death benefit rider</li>
    </ul>
  </div>
  <div class="tab" style="left:212px;top:177px;width:63px;height:13px;font-size:10.5px;line-height:13px;">Benefits:</div>

  <h2 class="title-red" style="left:19px;top:222px;font-size:8px;">Final Expense Insurance</h2>
  <p class="copy" style="left:19px;top:237px;width:178px;font-size:5.4px;line-height:7.2px;">Final Expense Insurance is a type of permanent whole life insurance insurance where the death benefit is used to cover (but not limited to) medical costs, funeral costs and other end-of-life expenses. It is a budget friendly option with a death benefit of up to $40k.</p>
  <div class="rate" style="left:19px;top:276px;font-size:5px;line-height:8px;"><span class="label" style="width:117px;padding-left:4px;">Monthly premiums as low as</span><span class="value" style="width:55px;margin-left:2px;">$11*</span></div>
  <div class="rate" style="left:19px;top:289px;font-size:5px;line-height:8px;"><span class="label" style="width:117px;padding-left:4px;">Death Benefits as high as</span><span class="value" style="width:55px;margin-left:2px;">$40,000</span></div>
  <p class="copy" style="left:19px;top:311px;width:180px;font-size:5.4px;line-height:7.2px;">Unforeseen events and a lack of the right kind of insurance can spell trouble quickly. Contact us today, to set up a free assessment time. We will analyze your insurance needs and get you and your family the right coverage quickly at a budget friendly price.</p>
  <p class="copy" style="left:19px;top:347px;width:180px;font-size:5.4px;line-height:7.2px;">We have been helping clients in Northern Idaho/Eastern Washington prepare for the unknown.</p>
  <p class="copy" style="left:19px;top:369px;width:180px;font-size:5.4px;line-height:7.2px;">We have access to the industry's top insurance carriers so you can get the right coverage, that fits your budget.</p>
  <p class="copy" style="left:19px;top:390px;width:184px;font-size:5.4px;line-height:7.2px;">Find out how we can give you the peace of mind of knowing your family will not have a financial burden if something were to happen to you.</p>

  <h2 class="title-red" style="left:223px;top:346px;font-size:8px;">We Also Specialize In:</h2>
  <ul class="ticks red-ticks" style="position:absolute;left:223px;top:361px;font-size:6px;line-height:10.8px;">
    <li style="padding-left:10px;">Medicare Supplement Insurance (Medigap)</li>
    <li style="padding-left:10px;">Annuities</li>
    <li style="padding-left:10px;">Mortgage Protection Insurance</li>
  </ul>
  <p class="note" style="left:223px;top:398px;width:134px;font-size:4.2px;line-height:5.5px;">*Based on an insured that is a 65 year old, non-smoking female that has no medical conditions with a death benefit of $2k</p>

  <div class="contact" style="left:20px;top:432px;font-size:12px;">Call us now:</div>
  <div class="contact" style="left:19px;top:444px;font-size:19.5px;">(208)555.0147</div>
  <span class="icon-ring" style="left:166px;top:446px;width:12px;height:12px;"></span>
  <div class="contact" style="left:184px;top:449px;font-size:5px;">tkerlow@harborvaleassurance.com</div>
  <span class="icon-ring" style="left:280px;top:446px;width:12px;height:12px;"></span>
  <div class="contact" style="left:297px;top:449px;font-size:5px;">harborvaleassurance.com</div>
  <div class="social" style="left:345px;top:463px;"><span style="width:5px;height:5px;"></span><span style="width:5px;height:5px;"></span></div>
</section>

<section class="sheet card-front" style="left:40px;top:823px;width:347px;height:235px;">
  <div class="photo" role="img" aria-label="Photo of a smiling young couple outdoors, man giving woman a piggyback ride" style="left:0;top:0;width:347px;height:150px;"></div>
  <svg class="layer" width="347" height="235" viewBox="0 0 347 235" aria-hidden="true">
    <path d="M0 0 H156 C144 30 98 58 0 58 Z" fill="#fff"/>
    <path d="M0 55 C95 55 140 28 152 0" fill="none" stroke="#231f20" stroke-width="3"/>
    <path d="M0 60 C100 60 148 32 160 0" fill="none" stroke="#e30613" stroke-width="1.6"/>
    <path d="M0 134 C70 150 200 140 347 116 V235 H0 Z" fill="#fff"/>
    <path d="M0 128 C70 144 200 134 347 110" fill="none" stroke="#231f20" stroke-width="4"/>
    <path d="M0 133 C70 149 200 139 347 115" fill="none" stroke="#e30613" stroke-width="2"/>
    <rect x="0" y="226" width="347" height="9" fill="#e30613"/>
  </svg>
  <div class="brand" style="left:28px;top:22px;font-size:7px;">Harborvale Assurance</div>
  <h1 class="headline" style="left:26px;top:72px;font-size:20.5px;">OUR<br><span class="accent">PLANS ARE</span><span class="sub" style="font-size:12px;">BASED ON YOURS</span></h1>
  <div class="benefits" style="left:190px;top:98px;width:137px;height:120px;border-radius:6px;">
    <ul class="ticks" style="position:absolute;left:6px;top:23px;width:128px;font-size:4px;line-height:5.2px;font-weight:500;">
      <li style="padding-left:7px;margin-bottom:6px;">All plans we offer are state regulated</li>
      <li style="padding-left:7px;margin-bottom:6px;">Relatively low monthly premiums</li>
      <li style="padding-left:7px;margin-bottom:6px;">Premiums can never increase</li>
      <li style="padding-left:7px;margin-bottom:6px;">Your policy can never be cancelled as long as you pay your premium</li>
      <li style="padding-left:7px;margin-bottom:6px;">No medical exams</li>
      <li style="padding-left:7px;margin-bottom:6px;">Guaranteed Death Benefit</li>
      <li style="padding-left:7px;">Many policies we offer are Guaranteed Acceptance, "Day 1" coverage, have a child/grandchild rider and/or have an accelerated death benefit rider</li>
    </ul>
  </div>
  <div class="tab" style="left:187px;top:107px;width:33px;height:7px;font-size:4.5px;line-height:7px;">Benefits:</div>
  <h2 class="title-red" style="left:25px;top:154px;font-size:8px;">Final Expense Insurance</h2>
  <p class="copy" style="left:25px;top:166px;width:158px;font-size:4px;line-height:5.2px;">Final Expense Insurance is a type of permanent whole life insurance where the death benefit is used to cover (but not limited to) medical costs, funeral costs and other end-of-life expenses. It is a budget friendly option with a death benefit of up to $40k.</p>
  <div class="rate" style="left:26px;top:193px;font-size:4px;line-height:7px;"><span class="label" style="width:67px;padding-left:3px;">Monthly premiums as low as</span><span class="value" style="width:30px;margin-left:4px;">$11*</span></div>
  <div class="rate" style="left:26px;top:203px;font-size:4px;line-height:7px;"><span class="label" style="width:67px;padding-left:3px;">Death Benefits as high as</span><span class="value" style="width:30px;margin-left:4px;">$40,000</span></div>
</section>

<section class="sheet card-back" style="left:404px;top:823px;width:348px;height:235px;">
  <div class="layer" style="left:196px;top:0;width:152px;height:235px;background:#fff;box-shadow:-3px 0 5px rgba(0,0,0,.12);"></div>
  <svg class="layer" width="197" height="235" viewBox="0 0 197 235" aria-hidden="true">
    <defs><linearGradient id="backRed" x1="0" y1="0" x2="0" y2="1"><stop offset="0" stop-color="#e30613"/><stop offset="1" stop-color="#9e1a1e"/></linearGradient></defs>
    <path d="M0 177 C60 163 130 175 196 167 V235 H0 Z" fill="url(#backRed)"/>
    <path d="M0 172 C60 158 130 170 196 162" fill="none" stroke="#231f20" stroke-width="2.5"/>
    <line x1="110" y1="28" x2="110" y2="48" stroke="#e30613" stroke-width="1"/>
    <line x1="23" y1="196" x2="66" y2="196" stroke="#fff" stroke-width=".6"/>
  </svg>
  <div class="brand" style="left:26px;top:33px;font-size:7.5px;">Harborvale Assurance</div>
  <p class="copy" style="left:119px;top:33px;font-size:5.4px;line-height:7px;color:var(--black);">PO Box 412<br>Pine Hollow, ID 83800</p>
  <p class="copy" style="left:22px;top:63px;width:165px;font-size:3.9px;line-height:5px;">We have been helping clients in Northern Idaho/Eastern Washington prepare for the unknown.</p>
  <p class="copy" style="left:22px;top:80px;width:165px;font-size:3.9px;line-height:5px;">We have access to the industry's top insurance carriers so you can get the right coverage, that fits your budget.</p>
  <p class="copy" style="left:22px;top:96px;width:165px;font-size:3.9px;line-height:5px;">Find out how we can give you the peace of mind of knowing your family will not have a financial burden if something were to happen to you.</p>
  <h2 class="title-red" style="left:22px;top:113px;font-size:5px;">We Also Specialize In:</h2>
  <ul class="ticks red-ticks" style="position:absolute;left:22px;top:123px;font-size:3.9px;line-height:6px;">
    <li style="padding-left:7px;">Medicare Supplement Insurance (Medigap)</li>
  </ul>
  <ul class="ticks red-ticks" style="position:absolute;left:135px;top:123px;font-size:3.9px;line-height:6px;">
    <li style="padding-left:7px;">Annuities</li>
  </ul>
  <ul class="ticks red-ticks" style="position:absolute;left:22px;top:135px;font-size:3.9px;line-height:6px;">
    <li style="padding-left:7px;">Mortgage Protection Insurance</li>
  </ul>
  <p class="note" style="left:77px;top:150px;width:112px;font-size:3px;line-height:4px;">*Based on an insured that is a 65 year old, non-smoking female that has no medical conditions with a death benefit of $2k</p>
  <div class="contact" style="left:23px;top:178px;font-size:7px;line-height:8.5px;font-weight:400;">GUARANTEED<br>APPROVAL!</div>
  <div class="contact" style="left:22px;top:200px;font-size:7px;">Call us now:</div>
  <div class="contact" style="left:22px;top:207px;font-size:11px;">(208)555.0147</div>
  <span class="icon-ring" style="left:104px;top:199px;width:9px;height:9px;"></span>
  <div class="contact" style="left:115px;top:201px;font-size:4px;">tkerlow@harborvaleassurance.com</div>
  <span class="icon-ring" style="left:104px;top:212px;width:9px;height:9px;"></span>
  <div class="contact" style="left:115px;top:214px;font-size:4px;">harborvaleassurance.com</div>
  <div class="social" style="left:174px;top:215px;"><span style="width:4.5px;height:4.5px;"></span><span style="width:4.5px;height:4.5px;"></span></div>
</section>
</body>
</html>
```